Torvel & Company: Business Cards, Stationery & Envelopes
Our Tagline is "Be Heard."
Simple
Marla Drosset
Founder, Torvel & Company
217 Meadow Lantern Dr.
Chapel Hill, North Carolina 27584
2816 Halloway Brook, NE
Atlanta, Georgia 30361
Marla@TorvelAndCo.example
www.TorvelAndCo.example
My consulting firm helps CEOs and other high-level executives with high-stakes communications. Our materials must exude professionalism and a modern, fresh, crisp and clean feel. The business cards, stationery and envelopes should match the look and feel of the logo and website. I'm interested in seeing designs that incorporate our "Be Heard" tagline, as well as ones that don't.
I think I prefer a card that is single-sided, but if you think there's a cool design that puts some information such as our addresses on back, I'm open to it.
Here are the relevant logo files

```html
<!DOCTYPE html>
<html lang="en">
<head>
<meta charset="utf-8">
<title>Torvel &amp; Company — Business Cards</title>
<link href="https://fonts.googleapis.com/css2?family=Cinzel:wght@400;600&display=swap" rel="stylesheet">
<style>
  :root {
    --page: #ffffff;
    --frame: #c9c9c9;
    --ink: #3a3a3a;
    --ink-soft: #555555;
    --red: #d8141b;
    --red-deep: #8e0308;
    --red-bright: #f2262c;
    --black: #111111;
    --charcoal: #4a4a4a;
    --white: #ffffff;
  }
  * { margin: 0; padding: 0; box-sizing: border-box; }
  html, body {
    width: 1200px; height: 734px; overflow: hidden;
    background: var(--page);
    font-family: "Cinzel", "Times New Roman", serif;
  }
  .sheet { position: relative; width: 1200px; height: 734px; }
  .card {
    position: absolute; width: 572px; height: 336px;
    border: 1px solid var(--frame); overflow: hidden;
  }
  .card--front { left: 20px; top: 22px; background: var(--white); }
  .card--red { left: 608px; top: 22px;
    background: radial-gradient(ellipse 70% 80% at 45% 55%, var(--red-bright) 0%, var(--red) 40%, var(--red-deep) 100%); }
  .card--white { left: 20px; top: 378px;
    background: radial-gradient(ellipse 45% 60% at 60% 40%, #f6f0f0 0%, var(--white) 100%); }
  .card--dark { left: 608px; top: 378px;
    background: radial-gradient(ellipse 60% 75% at 40% 55%, #8a8a8a 0%, var(--charcoal) 35%, var(--black) 100%); }

  .card__art { position: absolute; inset: 0; width: 100%; height: 100%; }

  .wordmark { position: absolute; display: flex; align-items: center; gap: 10px; }
  .wordmark__dot { width: 34px; height: 34px; border-radius: 50%; background: var(--red); }
  .wordmark__name { font-weight: 600; font-size: 22px; letter-spacing: 0.5px; }
  .wordmark--dark .wordmark__name { color: var(--ink); }
  .wordmark--light .wordmark__name { color: var(--white); }
  .wordmark--light .wordmark__dot { background: var(--white); }
  .card--dark .wordmark__dot { background: var(--red); }

  .card--front .wordmark { left: 26px; top: 22px; }
  .card--red .wordmark { left: 150px; top: 150px; }
  .card--white .wordmark { left: 150px; top: 148px; }
  .card--dark .wordmark { left: 145px; top: 150px; }

  .identity { position: absolute; right: 26px; top: 40px; text-align: right; }
  .identity__name { color: var(--red); font-size: 24px; font-weight: 400; line-height: 1.1; }
  .identity__role { color: var(--ink-soft); font-size: 13px; letter-spacing: 0.6px; margin-top: 4px; }

  .contact {
    position: absolute; right: 26px; top: 178px; text-align: right;
    color: var(--white); font-size: 11px; line-height: 14px; letter-spacing: 0.3px;
    font-style: normal;
  }
  .contact__block { margin-bottom: 10px; }
  .contact__block:last-child { margin-bottom: 0; }
</style>
</head>
<body>
<main class="sheet">

  <section class="card card--front" aria-label="Card front">
    <svg class="card__art" viewBox="0 0 572 336" preserveAspectRatio="none" aria-hidden="true">
      <defs>
        <radialGradient id="frontRed" cx="0.55" cy="0.85" r="0.8">
          <stop offset="0" stop-color="#f2262c"/>
          <stop offset="0.5" stop-color="#d8141b"/>
          <stop offset="1" stop-color="#8e0308"/>
        </radialGradient>
      </defs>
      <path d="M0,150 Q260,200 572,112 L572,336 L0,336 Z" fill="#111111"/>
      <path d="M0,176 Q270,222 572,140 L572,336 L0,336 Z" fill="url(#frontRed)"/>
    </svg>
    <div class="wordmark wordmark--dark">
      <span class="wordmark__dot"></span>
      <span class="wordmark__name">Torvel &amp; Company</span>
    </div>
    <div class="identity">
      <h1 class="identity__name">Marla Drosset</h1>
      <p class="identity__role">Founder, Torvel &amp; Company</p>
    </div>
    <address class="contact">
      <p class="contact__block">217 Meadow Lantern Dr.<br>Chapel Hill, North Carolina 27584</p>
      <p class="contact__block">2816 Halloway Brook, NE<br>Atlanta, Georgia 30361</p>
      <p class="contact__block">Cell: 404.555.0172<br>Email: Marla@TorvelAndCo.example<br>www.TorvelAndCo.example</p>
    </address>
  </section>

  <section class="card card--red" aria-label="Card back, red">
    <div class="wordmark wordmark--light">
      <span class="wordmark__dot"></span>
      <span class="wordmark__name">Torvel &amp; Company</span>
    </div>
  </section>

  <section class="card card--white" aria-label="Card back, white">
    <div class="wordmark wordmark--dark">
      <span class="wordmark__dot"></span>
      <span class="wordmark__name">Torvel &amp; Company</span>
    </div>
  </section>

  <section class="card card--dark" aria-label="Card back, dark">
    <div class="wordmark wordmark--light">
      <span class="wordmark__dot"></span>
      <span class="wordmark__name">Torvel &amp; Company</span>
    </div>
  </section>

</main>
</body>
</html>
```